Business card design needed

I need a business card that sets my business apart from big gyms and intimidating personal trainers. My personal training business focuses on outdoor and client in-home training, in an environment that is both enjoyable and sustainable for the client.
I train males and females, however a large proportion of my clientelle are female, so I would like the card to lean towards females, but still have a bit of masculine appeal about it.
My business colours are a deep sky blue and lightish red/orange (as seen in logo)

Contact Information for Business Card

Brightpath Wellness Coach
Discover a happier, healthier you!
Benedict Harlow- Health and Fitness Professional
Locations all across the Yarra Valley and Eastern Suburbs of Melbourne
0498315260
benedictharlowpt@quillmail.com.au

Requirements
Must have
• - Mobile number must stand out
- The 'Locations all across the Yarra Valley and Eastern Suburbs of Melbourne' must be clear and easy to read (different colour maybe?)

```html
<!DOCTYPE html>
<html lang="en">
<head>
<meta charset="utf-8">
<title>Brightpath Wellness Coach – Business Card</title>
<link rel="stylesheet" href="https://fonts.googleapis.com/css2?family=Arimo:wght@400;700&display=swap">
<style>
  :root {
    --stage: #2b2b2d;
    --navy: #0e2233;
    --deep-sky: #1f4a66;
    --sky-glow: #8fc3d8;
    --coral: #e2542a;
    --coral-deep: #c8461f;
    --ink: #111a22;
    --white: #ffffff;
  }
  * { margin: 0; padding: 0; box-sizing: border-box; }
  html, body {
    width: 1200px; height: 900px; overflow: hidden;
    background: var(--stage);
    font-family: "Arimo", Arial, sans-serif;
  }
  .stage { position: relative; width: 1200px; height: 900px; }

  .card {
    position: absolute;
    width: 540px; height: 308px;
    overflow: hidden;
    box-shadow: 0 14px 40px rgba(0,0,0,0.55);
  }

  /* Front: contact side */
  .card-front {
    left: 40px; top: 470px;
    background: radial-gradient(ellipse 70% 80% at 30% 70%, var(--sky-glow) 0%, #4b86a3 35%, var(--deep-sky) 65%, var(--navy) 100%);
  }
  .front-disc-shadow {
    position: absolute; left: 300px; top: -6px;
    width: 250px; height: 250px; border-radius: 50%;
    background: #000;
  }
  .front-disc {
    position: absolute; left: 310px; top: -16px;
    width: 250px; height: 250px; border-radius: 50%;
    background: radial-gradient(circle at 40% 40%, var(--coral) 0%, var(--coral-deep) 100%);
  }
  .call-line {
    position: absolute; left: 36px; top: 78px;
    color: var(--coral); font-size: 22px; letter-spacing: 1.5px;
  }
  .locations-band {
    position: absolute; left: 0; top: 132px;
    width: 400px; height: 70px;
    background: var(--coral);
    box-shadow: 0 4px 8px rgba(0,0,0,0.45);
    display: flex; align-items: center;
    padding-left: 24px;
    color: var(--white); font-size: 13.5px; line-height: 1.35;
  }
  .person-name {
    position: absolute; left: 90px; top: 226px;
    color: var(--ink); font-size: 22px;
  }
  .person-email {
    position: absolute; left: 36px; top: 268px;
    color: var(--ink); font-size: 17px;
  }

  /* Back: brand side */
  .card-back {
    left: 620px; top: 150px;
    background: radial-gradient(ellipse 60% 75% at 45% 40%, #b6dbe8 0%, #6fa7c1 30%, var(--deep-sky) 65%, var(--navy) 100%);
    display: flex; flex-direction: column; align-items: center;
  }
  .brand-disc {
    margin-top: 36px;
    width: 130px; height: 130px; border-radius: 50%;
    background: var(--coral);
    box-shadow: 4px 6px 0 #0b141c;
  }
  .brand-name {
    margin-top: 22px;
    color: var(--ink); font-size: 27px; font-weight: 700; letter-spacing: 0.5px;
  }
  .brand-tagline {
    margin-top: 14px;
    color: var(--coral); font-size: 19px; font-weight: 700; letter-spacing: 0.8px;
  }
</style>
</head>
<body>
<main class="stage">

  <section class="card card-front" aria-label="Business card, contact side">
    <div class="front-disc-shadow"></div>
    <div class="front-disc"></div>
    <p class="call-line">CALL&nbsp; 0498315260</p>
    <p class="locations-band">Health and Fitness Professional Locations all across<br>the Yarra Valley and Eastern Suburbs of Melbourne</p>
    <p class="person-name">Benedict Harlow</p>
    <p class="person-email">benedictharlowpt@quillmail.com.au</p>
  </section>

  <section class="card card-back" aria-label="Business card, brand side">
    <div class="brand-disc"></div>
    <p class="brand-name">Brightpath Wellness Coach</p>
    <p class="brand-tagline">Discover a happier, healthier you!</p>
  </section>

</main>
</body>
</html>
```